Vortane Labs - Methylene Blue Product Packaging

Our brand is Vortane Labs. We are launching a new product that is Methylene Blue, you can see more about this product if you search on Brisko or Pelludo and you will see what it is. This will be for a 50ml bottle. Give me different options for packaging that is minimalist and clean for this brand that makes it look well made and make people want to buy. I've added examples of what the bottle shape will be and potential packaging shapes so you can make packaging on those based off of that.

```html
<!DOCTYPE html>
<html lang="en">
<head>
<meta charset="UTF-8">
<title>Vortane Labs – Methylene Blue 1% Label</title>
<link rel="stylesheet" href="https://fonts.googleapis.com/css2?family=Inter:wght@700;800&family=Poppins:wght@500;600&display=swap">
<style>
  :root {
    --backdrop: #e9e8e9;
    --label: #f4f4f4;
    --ink: #1a1a1a;
    --ink-soft: #3a3a3a;
    --paper: #ffffff;
  }
  * { margin: 0; padding: 0; box-sizing: border-box; }
  html, body {
    width: 1200px;
    height: 1200px;
    overflow: hidden;
    background: var(--backdrop);
  }
  .canvas {
    width: 1200px;
    height: 1200px;
    display: flex;
    align-items: center;
    justify-content: center;
  }
  .label {
    width: 640px;
    height: 1000px;
    background: var(--label);
    display: flex;
    flex-direction: column;
    align-items: center;
    box-shadow: 0 2px 10px rgba(0,0,0,0.06);
  }
  .top-bar {
    margin-top: 90px;
    width: 400px;
    height: 44px;
    flex-shrink: 0;
  }
  .brand {
    margin-top: 56px;
    font-family: "Poppins", sans-serif;
    font-weight: 600;
    font-size: 46px;
    letter-spacing: -0.5px;
    color: var(--ink-soft);
    line-height: 1;
  }
  .product-name {
    margin-top: 110px;
    font-family: "Inter", sans-serif;
    font-weight: 800;
    font-size: 92px;
    line-height: 1.02;
    letter-spacing: 1px;
    color: var(--ink);
    text-align: center;
  }
  .strength {
    margin-top: 18px;
    font-family: "Inter", sans-serif;
    font-weight: 800;
    font-size: 74px;
    line-height: 1;
    color: var(--ink);
  }
  .benefit {
    margin-top: 40px;
    background: var(--ink);
    color: var(--paper);
    font-family: "Poppins", sans-serif;
    font-weight: 500;
    font-size: 28px;
    letter-spacing: 0.4px;
    padding: 10px 18px;
    line-height: 1.3;
  }
  .volume {
    margin-top: auto;
    margin-bottom: 22px;
    font-family: "Poppins", sans-serif;
    font-weight: 600;
    font-size: 30px;
    line-height: 1.2;
    color: var(--ink-soft);
  }
  .base {
    width: 100%;
    flex-shrink: 0;
  }
  .base-rule {
    height: 4px;
    background: var(--ink);
  }
  .base-rule + .base-rule { margin-top: 8px; }
  .base-band {
    margin-top: 8px;
    height: 120px;
    background: var(--ink);
  }
</style>
</head>
<body>
  <main class="canvas">
    <section class="label">
      <svg class="top-bar" viewBox="0 0 400 44" aria-hidden="true">
        <path d="M0 0 H400 Q396 44 370 44 H30 Q4 44 0 0 Z" fill="#1a1a1a"/>
      </svg>
      <div class="brand">Vortane Labs</div>
      <h1 class="product-name">Methylene<br>Blue</h1>
      <div class="strength">1%</div>
      <div class="benefit">Improves Brain Performance</div>
      <div class="volume">50 ml. (1.69 fl oz)</div>
      <div class="base">
        <div class="base-rule"></div>
        <div class="base-rule"></div>
        <div class="base-band"></div>
      </div>
    </section>
  </main>
</body>
</html>
```